IT Company, Needs new Logo and Letterhead Design

We need a Letterhead and possible a new logo for an existing IT Company. We are not happy with our current Letterhead that we are using in our quotes etc. We are happy to change our logo if required. We will upload our current logo and letterhead and look forward to getting some examples. We provide Server, Workstation and network support.

Target Market(s)

Small to Medium Sized Businesses.

Industry/Entity Type

It Company

Requirements
Must have
• Ability to edit the letterhead at a later date. Will need the source files for editing once approved.
Nice to have
• Same colour scheme, but we are open to suggestions.

```html
<!DOCTYPE html>
<html lang="en">
<head>
<meta charset="utf-8">
<title>Corvane Network Solutions – Letterhead and Logo</title>
<link rel="stylesheet" href="https://fonts.googleapis.com/css2?family=Jost:wght@500&family=Open+Sans:wght@400&family=Arimo:wght@400&display=swap">
<style>
  :root {
    --brand-orange: #f7941d;
    --ink-dark: #3f3f3f;
    --label-black: #111111;
    --sheet-white: #ffffff;
    --board-grey: #d0d0d0;
  }
  * { margin: 0; padding: 0; box-sizing: border-box; }
  html, body { width: 1200px; height: 1000px; overflow: hidden; }
  body { position: relative; background: var(--sheet-white); }

  .letterhead-panel {
    position: absolute; left: 0; top: 0; width: 1200px; height: 453px;
    background: var(--sheet-white);
  }
  .logo-panel {
    position: absolute; left: 0; top: 453px; width: 1200px; height: 547px;
    background: var(--board-grey);
  }
  .panel-label {
    position: absolute; left: 33px;
    font-family: "Arimo", Arial, sans-serif; font-size: 40px; font-weight: 400;
    color: var(--label-black); line-height: 1;
  }
  .letterhead-panel .panel-label { top: 370px; }
  .logo-panel .panel-label { top: 35px; }

  .brand-name {
    position: absolute;
    font-family: "Jost", "Futura", sans-serif; font-weight: 500;
    color: var(--brand-orange); line-height: 1.05;
  }
  .letterhead-brand { left: 33px; top: 118px; font-size: 22px; width: 110px; }
  .logo-brand { right: 83px; top: 610px; font-size: 56px; text-align: right; }

  .contact-block {
    position: absolute; top: 147px;
    font-family: "Open Sans", Arial, sans-serif; font-size: 13.5px;
    color: var(--ink-dark); line-height: 18px; white-space: nowrap;
  }
  .contact-address { left: 381px; }
  .contact-phones { left: 1008px; }

  .rule {
    position: absolute; left: 141px; width: 1014px;
    background: var(--brand-orange);
  }
  .rule-heavy { top: 207px; height: 8px; }
  .rule-medium { top: 223px; height: 6px; }
  .rule-fine { top: 241px; height: 2px; }
</style>
</head>
<body>
  <section class="letterhead-panel">
    <div class="brand-name letterhead-brand">Corvane Network Solutions</div>
    <div class="contact-block contact-address">
      <p>PO BOX 2841, HARBOURVIEW MALL, QLD 4590, 12 Tallow Street Kinrossie</p>
      <p>58 Ferrell Street. Ashgrove Bay</p>
    </div>
    <div class="contact-block contact-phones">
      <p>PHONE: 1300 555 014</p>
      <p>MOB: 0400 555 271</p>
    </div>
    <div class="rule rule-heavy"></div>
    <div class="rule rule-medium"></div>
    <div class="rule rule-fine"></div>
    <h2 class="panel-label">Letterhead</h2>
  </section>

  <section class="logo-panel">
    <h2 class="panel-label">Logo</h2>
  </section>
  <div class="brand-name logo-brand">Corvane<br>Network Solutions</div>
</body>
</html>
```